Webbanner-Design für Beteiligungsunternehmen
Zielgruppe
Ich habe ein kleines Familieninternes Beteiligungsunternehmen welches an verschiedenen Firmen beteiligt ist.
Aufgabenstellung
Ich brauche ein Profilbanner für Facebook und Twitter welches zum einen meine Hauptmarke 'Mertlow Holding' und meine Unternehmen an denen ich beteiligt bin (Geldwacht/Kaldoran Real Estate/ Velmora Holding/Brivalo) zeigt.

```html
<!DOCTYPE html>
<html lang="de">
<head>
<meta charset="utf-8">
<title>Mertlow Holding – Profilbanner</title>
<link rel="stylesheet" href="https://fonts.googleapis.com/css2?family=Oswald:wght@500;600&display=swap">
<style>
  :root {
    --white: #ffffff;
    --navy-deep: #0b1f4a;
    --navy: #1a3f80;
    --blue-bright: #5fa8f4;
    --sky: #b4dcff;
    --glow: rgba(120, 190, 255, 0.85);
    --frame-fill: rgba(10, 30, 70, 0.35);
  }
  * { margin: 0; padding: 0; box-sizing: border-box; }
  html, body { width: 1200px; height: 457px; overflow: hidden; background: var(--navy-deep); }
  .banner {
    position: relative;
    width: 1200px;
    height: 457px;
    overflow: hidden;
    font-family: "Oswald", "Arial Narrow", sans-serif;
    color: var(--white);
  }
  .banner__backdrop {
    position: absolute;
    inset: 0;
    background:
      radial-gradient(ellipse 240px 420px at 0% 50%, var(--sky) 0%, rgba(95,168,244,0.6) 45%, transparent 100%),
      radial-gradient(ellipse 240px 420px at 100% 50%, var(--sky) 0%, rgba(95,168,244,0.6) 45%, transparent 100%),
      radial-gradient(ellipse 300px 260px at 50% 42%, rgba(95,168,244,0.55) 0%, transparent 100%),
      radial-gradient(ellipse 520px 380px at 50% 60%, var(--navy) 0%, var(--navy-deep) 75%),
      var(--navy-deep);
  }

  /* Hauptmarke */
  .brand-main {
    position: absolute;
    left: 442px;
    top: 16px;
    width: 262px;
    display: flex;
    flex-direction: column;
    align-items: center;
    gap: 6px;
  }
  .brand-main__mark { width: 34px; height: 34px; background: var(--white); }
  .brand-main__name {
    font-size: 26px;
    font-weight: 500;
    letter-spacing: 1px;
    text-transform: uppercase;
    line-height: 1;
  }

  /* Beteiligungen */
  .partner {
    position: absolute;
    display: flex;
    align-items: center;
    font-weight: 500;
    text-transform: uppercase;
    line-height: 1;
  }
  .partner__mark { flex: none; background: var(--white); }

  .partner--geldwacht {
    left: 12px; top: 16px; width: 174px;
    flex-direction: column; gap: 10px;
    font-size: 27px;
  }
  .partner--geldwacht .partner__mark { width: 56px; height: 56px; border-radius: 50%; }

  .partner--kaldoran { left: 12px; top: 150px; gap: 10px; }
  .partner--kaldoran .partner__mark { width: 28px; height: 60px; }
  .partner__lines { display: flex; flex-direction: column; align-items: center; gap: 6px; }
  .partner__line-main { font-size: 19px; letter-spacing: 1px; }
  .partner__line-sub { font-size: 9px; letter-spacing: 3px; }

  .partner--brivalo { left: 1014px; top: 22px; gap: 8px; font-size: 34px; }
  .partner--brivalo .partner__mark { width: 34px; height: 34px; }

  .partner--velmora {
    left: 1008px; top: 86px; width: 184px;
    flex-direction: column; gap: 14px;
  }
  .partner--velmora .partner__mark { width: 54px; height: 92px; }
  .partner__ruled {
    display: flex; align-items: center; gap: 8px;
    font-size: 15px; letter-spacing: 3px; white-space: nowrap;
  }
  .partner__ruled::before, .partner__ruled::after {
    content: ""; width: 14px; height: 1px; background: var(--white);
  }

  /* Leistungsfelder */
  .services { list-style: none; }
  .service {
    position: absolute;
    display: flex;
    align-items: center;
    justify-content: center;
    border: 3px solid var(--white);
    background: var(--frame-fill);
    box-shadow: 0 0 10px var(--glow), inset 0 0 8px rgba(120,190,255,0.35);
    font-weight: 600;
    text-transform: uppercase;
    text-shadow: 0 0 10px var(--glow);
    line-height: 1;
  }
  .service--investment { left: 330px; top: 104px; width: 471px; height: 86px; font-size: 66px; }
  .service--realestate { left: 377px; top: 222px; width: 369px; height: 61px; font-size: 46px; }
  .service--stock { left: 417px; top: 320px; width: 293px; height: 45px; font-size: 33px; border-width: 2px; }
  .service--bonds { left: 449px; top: 401px; width: 231px; height: 37px; font-size: 27px; border-width: 2px; }
</style>
</head>
<body>
  <div class="banner">
    <div class="banner__backdrop" role="img" aria-label="Geschäftsmann im Anzug berührt einen leuchtenden virtuellen Bildschirm vor blauem Hintergrund"></div>

    <div class="brand-main">
      <span class="brand-main__mark"></span>
      <span class="brand-main__name">Mertlow Holding</span>
    </div>

    <div class="partner partner--geldwacht">
      <span class="partner__mark"></span>
      <span>Geldwacht</span>
    </div>

    <div class="partner partner--kaldoran">
      <span class="partner__mark"></span>
      <span class="partner__lines">
        <span class="partner__line-main">Kaldoran</span>
        <span class="partner__line-sub">Real Estate</span>
      </span>
    </div>

    <div class="partner partner--brivalo">
      <span class="partner__mark"></span>
      <span>Brivalo</span>
    </div>

    <div class="partner partner--velmora">
      <span class="partner__mark"></span>
      <span class="partner__ruled">Velmora Holding</span>
    </div>

    <ul class="services">
      <li class="service service--investment">Investment</li>
      <li class="service service--realestate">Real Estate</li>
      <li class="service service--stock">Stock</li>
      <li class="service service--bonds">Bonds</li>
    </ul>
  </div>
</body>
</html>
```